Verpackungsdesign für Nahrungsergänzungsmittel
Zielgruppe
Wir sind eine Firma für Nahrungsergänzungsmittel und suchen für unser neues Produkt ein Ansprechendes Etikett für die Dose. Das Produkt: GLANZ KRAFT KERN
Aufgabenstellung
Deckel: weiß, geriffelt
Etikettengröße: 145 x 50 mm
Folgender Inhalt muss auf die Dose: Siehe Screenshot 0012
Außerdem soll unser Logo drauf: Siehe Bild waldquellig.734.png
Bitte an folgenden Beispielen orientieren:
https://www.kaufhalle-beispiel.example/Lumetra-Glanz-Kraft-Hochdosiert-Vitalkomplex/dp/X00000000Q

```html
<!DOCTYPE html>
<html lang="de">
<head>
<meta charset="utf-8">
<title>Etikett GLANZ KRAFT KERN</title>
<link href="https://fonts.googleapis.com/css2?family=Titillium+Web:wght@400;600;700&family=Open+Sans:wght@400&display=swap" rel="stylesheet">
<style>
  :root {
    --green: #7cae45;
    --ink: #1b1b1b;
    --muted: #6d6d6d;
    --rule: #9a9a9a;
    --paper: #ffffff;
    --border: #dcdcdc;
  }
  html, body { margin: 0; padding: 0; overflow: hidden; }
  body {
    width: 1200px; height: 691px; background: var(--paper);
    font-family: "Titillium Web", sans-serif; color: var(--ink);
    position: relative;
  }
  .label {
    position: absolute; left: 50px; top: 155px; width: 1100px; height: 380px;
    border: 1px solid var(--border); box-sizing: border-box; background: var(--paper);
  }
  /* nutrition table */
  .nutrition { position: absolute; left: 56px; top: 32px; width: 252px; }
  .nutrition table {
    width: 100%; border-collapse: collapse; font-size: 8.5px; letter-spacing: .3px;
    text-transform: uppercase; color: var(--muted); border: 1px solid var(--rule);
  }
  .nutrition th {
    background: var(--green); color: #fff; font-weight: 700; text-align: left;
    padding: 5px 5px; line-height: 1.3; vertical-align: top; border-right: 1px solid #fff;
  }
  .nutrition th.num { text-align: right; }
  .nutrition td { padding: 5px 5px; border-top: 1px solid var(--rule); border-right: 1px solid var(--rule); line-height: 1.35; }
  .nutrition td.num { text-align: right; white-space: nowrap; }
  .nutrition .notes { font-size: 6px; line-height: 1.4; padding: 5px; text-transform: uppercase; color: var(--muted); border-top: 1px solid var(--rule); }
  /* front panel */
  .front { position: absolute; left: 404px; top: 0; width: 300px; text-align: center; }
  .brand-mark { width: 44px; height: 44px; border-radius: 50%; background: var(--green); margin: 40px auto 0; }
  .brand-name { margin-top: 30px; font-size: 23px; font-weight: 400; letter-spacing: .5px; line-height: 1; }
  .product-name { margin: 18px 0 0; font-size: 46px; font-weight: 700; line-height: 1.3; }
  .divider { width: 162px; height: 1.5px; background: var(--ink); margin: 4px auto 0; }
  .claim { margin-top: 6px; font-size: 20px; letter-spacing: 1px; font-weight: 400; }
  .category { margin-top: 4px; font-family: "Open Sans", sans-serif; font-size: 16px; color: #333; }
  /* info column */
  .info {
    position: absolute; left: 798px; top: 26px; width: 240px;
    font-size: 9.5px; line-height: 1.8; letter-spacing: .4px; text-transform: uppercase; color: var(--muted);
  }
  .info strong { font-weight: 700; }
  .info p { margin: 0 0 14px; }
  /* band */
  .count-band {
    position: absolute; left: 2px; right: 2px; top: 325px; height: 31px;
    background: var(--green); color: #fff; text-align: center;
    font-size: 19px; letter-spacing: 3px; line-height: 31px;
  }
</style>
</head>
<body>
  <section class="label">
    <div class="nutrition">
      <table>
        <tr><th>Nähr- und<br>Inhaltsstoffe</th><th class="num">Pro<br>Tagesdosis<br>(2 Kapseln)</th><th class="num">%<br>NRV*</th></tr>
        <tr><td>Pantothensäure</td><td class="num">6 mg</td><td class="num">100%</td></tr>
        <tr><td>Vitamin B6</td><td class="num">1,4 mg</td><td class="num">100%</td></tr>
        <tr><td>Biotin</td><td class="num">51 µg</td><td class="num">100%</td></tr>
        <tr><td>Kupfer</td><td class="num">1 mg</td><td class="num">100%</td></tr>
        <tr><td>Zink</td><td class="num">10 mg</td><td class="num">100%</td></tr>
        <tr><td>Polyporus umbellatus<br>davon Polysaccharide</td><td class="num">100 mg<br>30 mg</td><td class="num">**</td></tr>
        <tr><td>Bambussprossen<br>– davon Silizium</td><td class="num">43,5 mg<br>32,6 mg</td><td class="num">**</td></tr>
      </table>
      <div class="notes">* Prozent Nährstoffbezugswerte (NRV) laut Verordnung (EU) Nr. 1169/2011<br>** Keine Nährstoffbezugswerte (NRV) vorhanden</div>
    </div>

    <div class="front">
      <div class="brand-mark"></div>
      <div class="brand-name">WALDQUELLIG</div>
      <h1 class="product-name">GLANZ KRAFT<br>KERN</h1>
      <div class="divider"></div>
      <div class="claim">BIOTIN + ZINK</div>
      <div class="category">Nahrungsergänzungsmittel</div>
    </div>

    <div class="info">
      <p><strong>Zutaten:</strong> Perlhirse-Extrakt 4:1, Trennmittel: Magnesiumsalze der Speise-Fettsäuren, Überzugsmittel: Hydroxypropylmethylcellulose, Eichhase-Extrakt (Polyporus umbellatus; 30 % Polysaccharide), Zinkgluconat, Bambussprossen-Extrakt 5:1 (75 % Silizium), Kupfergluconat, Calcium-D-Pantothenat, Pyridoxinhydrochlorid, D-Biotin.</p>
      <p><strong>Verzehrempfehlung:</strong> 2 Kapseln täglich mit reichlich Flüssigkeit einnehmen.</p>
    </div>

    <div class="count-band">60 KAPSELN</div>
  </section>
</body>
</html>
```